LOGO for A Neighborhood Finance Center
BLUE LEDGER PLUS
Professional
HAROLD QUINCE and DENNIS HOLTBERG
Manger
3710 S Wexford st 204
Milledgeville GA 31061
BlueLEDGERPLUS@mailnook.example
BLUELEDGERPLUS.example
I need two versions one with Harold Quince
I need one with Dennis Holtberg

```html
<!DOCTYPE html>
<html lang="en">
<head>
<meta charset="utf-8">
<title>Blue Ledger Plus – Business Card</title>
<link rel="stylesheet" href="https://fonts.googleapis.com/css2?family=Montserrat:wght@500;600;700&family=Open+Sans:wght@400;600&display=swap">
<style>
  :root {
    --backdrop: #e9e6e1;
    --card: #ffffff;
    --brand-blue: #1f6fb7;
    --deep-blue: #0f4f96;
    --light-blue: #2fa3dc;
    --brand-green: #5bb544;
    --light-green: #8fd06a;
    --ink: #4a4f55;
    --muted: #8a8f95;
    --rule: #c9ccd0;
  }
  * { margin: 0; padding: 0; box-sizing: border-box; }
  html, body {
    width: 1200px; height: 914px; overflow: hidden;
    background: var(--backdrop);
  }
  .canvas {
    position: relative; width: 1200px; height: 914px;
    display: flex; align-items: center; justify-content: center;
  }
  .card {
    position: relative; width: 1000px; height: 572px;
    background: var(--card);
    box-shadow: 0 10px 30px rgba(0,0,0,.12);
    overflow: hidden;
  }
  .card-bands { position: absolute; inset: 0; }
  .brand {
    position: absolute; left: 0; right: 0; top: 150px;
    display: flex; align-items: center; justify-content: center; gap: 16px;
  }
  .brand-dot {
    width: 34px; height: 34px; border-radius: 50%;
    background: var(--brand-green);
  }
  .brand-name {
    font-family: 'Montserrat', sans-serif; font-weight: 700;
    font-size: 44px; letter-spacing: 1px; color: var(--brand-blue);
  }
  .identity {
    position: absolute; left: 150px; top: 300px; width: 310px;
    text-align: left;
  }
  .person-name {
    font-family: 'Montserrat', sans-serif; font-weight: 700;
    font-size: 22px; color: var(--brand-blue); letter-spacing: .5px;
  }
  .person-role {
    font-family: 'Open Sans', sans-serif; font-size: 16px;
    color: var(--muted); margin-top: 2px; padding-left: 70px;
  }
  .address {
    position: absolute; left: 150px; top: 395px;
    font-family: 'Open Sans', sans-serif; font-size: 17px;
    line-height: 25px; color: var(--ink);
  }
  .divider {
    position: absolute; left: 478px; top: 300px;
    width: 1px; height: 165px; background: var(--rule);
  }
  .contacts {
    position: absolute; left: 494px; top: 298px; list-style: none;
    font-family: 'Open Sans', sans-serif; font-size: 16px; color: var(--ink);
  }
  .contacts li { display: flex; align-items: center; gap: 8px; height: 25px; }
  .contact-icon { width: 17px; height: 17px; flex: none; }
</style>
</head>
<body>
<div class="canvas">
  <article class="card">
    <svg class="card-bands" width="1000" height="572" viewBox="0 0 1000 572" aria-hidden="true">
      <defs>
        <linearGradient id="blueBand" x1="0" x2="1" y1="0" y2="0">
          <stop offset="0" stop-color="var(--light-blue)"/>
          <stop offset="1" stop-color="var(--deep-blue)"/>
        </linearGradient>
        <linearGradient id="greenBand" x1="0" x2="1" y1="0" y2="0">
          <stop offset="0" stop-color="var(--light-green)"/>
          <stop offset="1" stop-color="var(--brand-green)"/>
        </linearGradient>
      </defs>
      <polygon points="0,368 462,368 478,392 0,392" fill="url(#blueBand)"/>
      <polygon points="0,392 478,392 470,400 0,400" fill="var(--deep-blue)" opacity=".35"/>
      <polygon points="478,488 1000,488 1000,520 500,520" fill="url(#greenBand)"/>
    </svg>

    <div class="brand">
      <span class="brand-dot"></span>
      <span class="brand-name">BLUE LEDGER PLUS</span>
    </div>

    <div class="identity">
      <p class="person-name">HAROLD QUINCE</p>
      <p class="person-role">Manger</p>
    </div>

    <address class="address">
      3710 S Wexford st 204<br>
      Milledgeville GA 31061
    </address>

    <div class="divider"></div>

    <ul class="contacts">
      <li>
        <svg class="contact-icon" viewBox="0 0 20 20"><circle cx="10" cy="10" r="10" fill="var(--ink)"/><path d="M6.5 5.5l2 2-1 1.3c.7 1.5 1.8 2.6 3.2 3.2l1.3-1 2 2-1.2 1.5C9.5 14.3 5.7 10.5 5.5 6.7z" fill="#fff"/></svg>
        5550142287
      </li>
      <li>
        <svg class="contact-icon" viewBox="0 0 20 20"><circle cx="10" cy="10" r="10" fill="var(--ink)"/><rect x="7" y="4.5" width="6" height="11" rx="1.2" fill="#fff"/><rect x="8" y="6" width="4" height="6.5" fill="var(--ink)"/></svg>
        5550193364
      </li>
      <li>
        <svg class="contact-icon" viewBox="0 0 20 20"><circle cx="10" cy="10" r="10" fill="var(--ink)"/><rect x="5" y="8" width="10" height="6" rx="1" fill="#fff"/><rect x="7" y="5" width="6" height="3.5" fill="#fff"/></svg>
        5550142287
      </li>
      <li>
        <svg class="contact-icon" viewBox="0 0 20 20"><circle cx="10" cy="10" r="10" fill="var(--ink)"/><rect x="5" y="6.5" width="10" height="7" fill="#fff"/><path d="M5 6.5l5 4 5-4" fill="none" stroke="var(--ink)" stroke-width="1.2"/></svg>
        BlueLEDGERPLUS@mailnook.example
      </li>
      <li>
        <svg class="contact-icon" viewBox="0 0 20 20"><circle cx="10" cy="10" r="10" fill="var(--ink)"/><circle cx="10" cy="10" r="5" fill="none" stroke="#fff" stroke-width="1.2"/><path d="M5 10h10M10 5c-2.5 3-2.5 7 0 10M10 5c2.5 3 2.5 7 0 10" fill="none" stroke="#fff" stroke-width="1"/></svg>
        BLUELEDGERPLUS.example
      </li>
    </ul>
  </article>
</div>
</body>
</html>
```